Visitenkarten für regionale Fluggesellschaft
Zielgruppe
Wir sind eine regionale Fluggesellschaft, die seit zehn Jahren Flüge von Mannheim aus anbietet.
Aufgabenstellung
Gern möchten wir das Design der bisherigen Visitenkarten überarbeiten lassen. Die bisherigen sind seit über fünf Jahren im Einsatz. Es darf moderner aussehen. Vielleicht auch mit Symbolen (wie Font Awesome) gearbeitet werden.
Die Adresse sollte sein:
LHV Lindenhof-Vogtmar Jet GmbH
Birkenweiler Talstr. 48
74391 Mannheim

```html
<!DOCTYPE html>
<html lang="de">
<head>
<meta charset="utf-8">
<title>Visitenkarte LHV Lindenhof-Vogtmar Jet</title>
<link href="https://fonts.googleapis.com/css2?family=Arimo:wght@400;700&display=swap" rel="stylesheet">
<style>
  :root {
    --backdrop: #c9c9cc;
    --paper: #ffffff;
    --blue: #008bd5;
    --blue-light: #7fc1ea;
    --blue-pale: #c4e1f6;
    --yellow: #f9df00;
    --lime: #b8cd44;
    --green: #22a548;
    --text-light: #6db8e8;
  }
  html, body {
    margin: 0;
    width: 1200px;
    height: 1200px;
    overflow: hidden;
    background: var(--backdrop);
    font-family: "Arimo", Arial, sans-serif;
  }
  .sheet {
    width: 1200px;
    height: 1200px;
    display: flex;
    flex-direction: column;
    align-items: center;
    justify-content: center;
    gap: 60px;
  }
  .card {
    position: relative;
    width: 720px;
    height: 466px;
    background: var(--paper);
    box-shadow: 0 6px 18px rgba(0,0,0,0.12);
    overflow: hidden;
  }
  .facet-area {
    position: absolute;
  }
  .facet-area--left {
    left: 0; top: 110px; width: 150px; height: 260px;
    background: linear-gradient(160deg, var(--blue) 0%, var(--blue-light) 35%, var(--blue-pale) 50%, var(--yellow) 70%, var(--lime) 100%);
    clip-path: polygon(0 10%, 100% 0, 100% 55%, 0 100%);
  }
  .facet-area--right {
    right: 0; top: 70px; width: 150px; height: 330px;
    background: linear-gradient(200deg, var(--green) 0%, var(--lime) 28%, var(--yellow) 48%, var(--blue) 68%, var(--blue-light) 100%);
    clip-path: polygon(100% 0, 100% 90%, 0 100%, 0 30%);
  }
  .contact {
    position: absolute;
    left: 190px;
    top: 120px;
    width: 360px;
    color: var(--text-light);
  }
  .contact__name {
    margin: 0 0 34px;
    font-size: 30px;
    font-weight: 700;
    color: var(--blue);
    white-space: nowrap;
  }
  .contact__lines {
    margin: 0;
    font-size: 20px;
    line-height: 1.36;
    white-space: nowrap;
  }
  .contact__web {
    margin: 36px 0 0;
    font-size: 20px;
    color: var(--green);
  }
  .brand-band {
    position: absolute;
    left: 0; top: 0; width: 720px; height: 260px;
    background: linear-gradient(90deg, var(--green) 0%, var(--lime) 30%, var(--yellow) 55%, var(--blue) 78%, var(--blue-light) 100%);
  }
  .brand-name {
    position: absolute;
    left: 0; right: 0; top: 320px;
    display: flex;
    align-items: center;
    justify-content: center;
    gap: 16px;
    font-size: 34px;
    font-weight: 400;
    color: var(--blue);
  }
  .brand-name__square {
    width: 22px; height: 22px;
    background: var(--blue);
  }
</style>
</head>
<body>
<main class="sheet">
  <section class="card card--front">
    <div class="facet-area facet-area--left" role="img" aria-label="Geometrische Faltflächen in Blau, Gelb und Grün"></div>
    <div class="facet-area facet-area--right" role="img" aria-label="Geometrische Faltflächen in Grün, Gelb und Blau"></div>
    <div class="contact">
      <h1 class="contact__name">Jonas Beispielmann</h1>
      <p class="contact__lines">
        LHV Lindenhof-Vogtmar Jet GmbH<br>
        Birkenweiler Talstr. 48<br>
        74391 Mannheim<br>
        T +49 (0)621 90 17 34 - 0<br>
        E reservierung@flyLHV.de
      </p>
      <p class="contact__web">www.flyLHV.de</p>
    </div>
  </section>
  <section class="card card--back">
    <div class="brand-band" role="img" aria-label="Große geometrische Faltflächen in Grün, Gelb und Blau"></div>
    <div class="brand-name">
      <span class="brand-name__square"></span>
      <span>Lindenhof-Vogtmar Jet</span>
    </div>
  </section>
</main>
</body>
</html>
```